Business card design needed

Hi,
I was hoping to have a business card designed with a background similar to dark coloured concrete texture. I have a photo of the particular concrete that I would like to be used as the background but for some reason it wouldn't let me upload the image. Please email me for the image and I will send to you asap.
I would like the company name to be in a font that is thin, crisp to reflect 'precision'. I am trying to convey that my services are more precise and have more attention to detail than my competitors. I would like this to be represented through the font if possible.
Colours are at your discretion - although we would like it to attract the eye and stand out. We would like the card to be in a modern style.
I was thinking for an image in the background of the card, or on the side of the card wherever is appropriate, half of a ring saw blade or similar.
The company is a concrete cutting and drilling service - we are a 24 hour 7 day service which is unique to the industry. We provide a more detailed service to our customers and this is the backbone of our reputation.
Target Market(s)
Construction industry & general public
Industry/Entity Type
Concrete
Contact Information for Business Card
Ridgeline Saw & Bore Pty Ltd
Concrete Cutting & Drilling
24 hour 7 day service
Trevor Halloway
Director
M: 0412 908 251
P: (07) 3196 4027
E: ridgelinesawandbore@mailbrook.example
PO Box 318, Wendaroo DC QLD 4172

```html
<!DOCTYPE html>
<html lang="en">
<head>
<meta charset="utf-8">
<title>Ridgeline Saw &amp; Bore — Business Card</title>
<link rel="stylesheet" href="https://fonts.googleapis.com/css2?family=Stardos+Stencil:wght@700&family=Saira+Extra+Condensed:wght@500;600&family=Open+Sans:ital,wght@1,400&display=swap">
<style>
  :root {
    --page-bg: #e9e7e3;
    --concrete-light: #3fa6c4;
    --concrete-mid: #2b8db0;
    --concrete-deep: #0f4f78;
    --card-white: #f3f4f5;
    --strip-grey: #d9dcde;
    --ink: #14181c;
    --ink-navy: #0b2438;
    --name-white: #f4f7f9;
  }
  html, body {
    margin: 0;
    width: 1200px;
    height: 900px;
    overflow: hidden;
    background: var(--page-bg);
  }
  .card {
    position: absolute;
    left: 100px;
    top: 164px;
    width: 1000px;
    height: 572px;
    background: var(--card-white);
    box-shadow: 0 12px 30px rgba(0,0,0,0.18);
    overflow: hidden;
  }
  .card-art { display: block; }
  .condensed {
    font-family: "Saira Extra Condensed", "Arial Narrow", sans-serif;
    text-transform: uppercase;
  }
  .holder-name { font-weight: 600; font-size: 36px; fill: var(--name-white); }
  .holder-role {
    font-family: "Open Sans", sans-serif;
    font-style: italic;
    font-size: 24px;
    fill: var(--name-white);
  }
  .service-main { font-weight: 600; font-size: 72px; fill: var(--ink); }
  .service-sub { font-weight: 500; font-size: 30px; fill: var(--ink); }
  .service-hours { font-weight: 600; font-size: 38px; fill: var(--ink); }
  .service-hours-note { font-weight: 500; font-size: 20px; fill: var(--ink); }
  .company {
    font-family: "Stardos Stencil", serif;
    font-weight: 700;
    font-size: 48px;
    fill: var(--ink);
  }
  .contact { font-weight: 500; font-size: 25px; fill: var(--ink-navy); }
</style>
</head>
<body>
  <article class="card">
    <svg class="card-art" viewBox="0 0 1000 572" width="1000" height="572">
      <defs>
        <radialGradient id="concrete-tone" cx="0.55" cy="0.25" r="0.9">
          <stop offset="0" stop-color="#3fa6c4"/>
          <stop offset="0.55" stop-color="#2b8db0"/>
          <stop offset="1" stop-color="#0f4f78"/>
        </radialGradient>
      </defs>
      <rect class="concrete-texture" role="img" aria-label="Blue-teal cracked concrete texture" x="0" y="0" width="1000" height="572" fill="url(#concrete-tone)"/>
      <path class="torn-base" fill="#f3f4f5"
            d="M0,555 L300,540 L470,522 L495,530 L510,568 L570,515 L700,480 L850,455 L1000,430 L1000,572 L0,572 Z"/>
      <path class="torn-strip" fill="#d9dcde" stroke="rgba(0,0,0,0.25)" stroke-width="1.5"
            d="M95,262 L230,250 L300,222 L360,232 L470,226 L560,214 L640,220 L700,205 L780,208 L830,212 L900,225 L925,262 L910,300 L820,318 L700,312 L610,330 L520,326 L430,340 L330,338 L250,352 L160,350 L100,340 L92,300 Z"/>

      <g class="holder">
        <text class="condensed holder-name" x="70" y="120" textLength="250" lengthAdjust="spacingAndGlyphs">Trevor Halloway</text>
        <text class="holder-role" x="70" y="152">Director</text>
      </g>

      <g class="service">
        <text class="condensed service-main" x="590" y="118" textLength="330" lengthAdjust="spacingAndGlyphs">Concrete</text>
        <text class="condensed service-sub" x="590" y="154" textLength="300" lengthAdjust="spacingAndGlyphs">Cutting &amp; Drilling</text>
        <text class="condensed service-hours" x="728" y="198" textLength="62" lengthAdjust="spacingAndGlyphs">24/7</text>
        <text class="condensed service-hours-note" x="794" y="198" textLength="126" lengthAdjust="spacingAndGlyphs">Hours Service</text>
      </g>

      <text class="company" x="130" y="300" textLength="760" lengthAdjust="spacingAndGlyphs">RIDGELINE SAW &amp; BORE PTY LTD</text>

      <g class="contact-lines">
        <text class="condensed contact" x="62" y="420" textLength="360" lengthAdjust="spacingAndGlyphs">PO Box 318, Wendaroo DC QLD 4172</text>
        <text class="condensed contact" x="62" y="450" textLength="150" lengthAdjust="spacingAndGlyphs">M: 0412 908 251</text>
        <text class="condensed contact" x="62" y="480" textLength="165" lengthAdjust="spacingAndGlyphs">P: (07) 3196 4027</text>
        <text class="condensed contact" x="62" y="510" textLength="390" lengthAdjust="spacingAndGlyphs">E: ridgelinesawandbore@mailbrook.example</text>
      </g>
    </svg>
  </article>
</body>
</html>
```